Email Marketing Campaign Templates

Email drip childcare campaign designed to communicate with parents interested in services. We would like the template(s) to be created so that we can change the content as needed.I will add below collateral that we have used in the past as well as logo.
three to for templates 1.) welcome template 2/ things to bring 3) generic template
Target Market(s)
Parents and Millennials
Industry/Entity Type
Childcare
Colors
85cae6
0493ce
9bcb3c
add136
fefefe
faa54b
cadf82
86cae7
33a6d7
Requirements
Must have
- Photos of staff with children
Nice to have
- Photos

```html
<!DOCTYPE html>
<html lang="en">
<head>
<meta charset="utf-8">
<title>Little Harbour Childcare – Newsletter</title>
<link href="https://fonts.googleapis.com/css2?family=Arimo:wght@400;700&display=swap" rel="stylesheet">
<style>
:root{
  --blue:#33a6d7;
  --blue-deep:#0493ce;
  --blue-soft:#85cae6;
  --green:#9bcb3c;
  --green-bright:#add136;
  --green-pale:#cadf82;
  --white:#fefefe;
  --ink:#1e1e1e;
  --grey-bg:#f5f5f5;
}
*{box-sizing:border-box;margin:0;padding:0}
html,body{width:1200px;height:4157px;overflow:hidden;background:var(--white)}
body{font-family:"Arimo",Arial,sans-serif;color:var(--ink);position:relative}
.section{position:absolute;left:0;width:1200px}
.btn{position:absolute;display:flex;align-items:center;justify-content:center;height:50px;border-radius:25px;background:var(--blue);color:var(--white);font-weight:700;font-size:23px;text-decoration:none}
.heading{font-weight:700;color:var(--ink)}
.column-text{font-size:20px;line-height:36px;color:var(--ink);white-space:nowrap}

/* header */
.header{top:0;height:222px;border-bottom:6px solid var(--green)}
.brand{position:absolute;left:0;width:1200px;top:74px;display:flex;align-items:center;justify-content:center;gap:14px}
.brand-dot{width:46px;height:46px;border-radius:50%;background:var(--green)}
.brand-name{font-size:36px;font-weight:700;color:var(--blue)}

/* hero */
.hero{top:222px;height:476px}
.hero-photo{position:absolute;inset:0;background:linear-gradient(90deg,#ffffff 0%,#f4efec 25%,#d9c2b3 50%,#c79c86 70%,#b5745e 88%,#d8bfae 100%)}
.hero-title{position:absolute;left:75px;top:82px;font-size:55px;line-height:68px}
.hero .btn{left:75px;top:332px;width:249px}

/* about */
.about{top:698px;height:493px;text-align:center}
.about-title{position:absolute;left:0;width:1200px;top:108px;font-size:50px}
.about-text{position:absolute;left:0;width:1200px;top:192px;font-size:20px;line-height:37px}
.about .btn{left:454px;top:341px;width:255px}

/* services */
.services{top:1191px;height:651px}
.services-bg{position:absolute;left:0;top:0;width:1200px;height:651px;background:var(--grey-bg)}
.services-photo{position:absolute;left:0;top:0}
.services-title{position:absolute;left:676px;top:100px;font-size:44px;line-height:66px}
.services-text{position:absolute;left:676px;top:276px}
.services .btn{left:668px;top:505px;width:255px}

/* checklist */
.checklist{top:1842px;height:721px}
.checklist-title{position:absolute;left:75px;top:142px;font-size:44px;line-height:67px}
.checklist-text{position:absolute;left:75px;top:302px}
.checklist .btn{left:78px;top:529px;width:252px}
.item{position:absolute;left:587px;width:560px;height:130px}
.item-icon{position:absolute;left:0;top:0;width:128px;height:128px}
.item-title{position:absolute;left:180px;top:0;font-size:21px;font-weight:700}
.item-text{position:absolute;left:180px;top:40px;font-size:18px;line-height:34px}

/* banner */
.banner{top:2563px;height:560px}
.banner-photo{position:absolute;inset:0;background:linear-gradient(120deg,#5fb4da 0%,#86cae7 45%,#4aa8d4 75%,#6fbde2 100%)}
.banner-title{position:absolute;left:0;width:1200px;top:148px;text-align:center;font-size:55px;font-weight:700;color:var(--white)}
.banner-text{position:absolute;left:0;width:1200px;top:253px;text-align:center;font-size:25px;line-height:49px;color:var(--white)}
.banner .btn{left:460px;top:388px;width:258px;height:61px;background:transparent;border:3px solid var(--white);border-radius:14px}

/* gallery */
.gallery{top:3123px;height:659px}
.gallery-title{position:absolute;left:86px;top:92px;font-size:44px;line-height:66px}
.gallery-text{position:absolute;left:86px;top:256px}
.gallery .btn{left:78px;top:485px;width:252px}
.snapshot{position:absolute;background:var(--white);box-shadow:0 6px 18px rgba(0,0,0,.28);padding:22px}
.snapshot-fill{width:100%;height:100%}
.snapshot-back{left:680px;top:70px;width:450px;height:300px;transform:rotate(9deg)}
.snapshot-back .snapshot-fill{background:linear-gradient(180deg,#bcd7ec 0%,#c9d8c4 45%,#6f9a4e 70%,#5b8a3c 100%)}
.snapshot-front{left:600px;top:270px;width:410px;height:345px;transform:rotate(-4deg)}
.snapshot-front .snapshot-fill{background:linear-gradient(160deg,#a6a58c 0%,#8e8a74 40%,#b98a72 70%,#9a7d66 100%)}

/* footer */
.footer{top:3782px;height:375px;background:var(--green);color:var(--white)}
.social{position:absolute;top:109px;width:61px;height:61px;border-radius:50%;background:var(--white)}
.contact{position:absolute;top:203px;left:0;width:1200px;height:30px;font-size:17px;font-weight:700;white-space:nowrap}
.contact span,.contact svg{position:absolute;top:2px}
.copyright{position:absolute;left:0;width:1200px;top:268px;text-align:center;font-size:15px}
</style>
</head>
<body>

<header class="section header">
  <div class="brand">
    <span class="brand-dot"></span>
    <span class="brand-name">Little Harbour Childcare</span>
  </div>
</header>

<section class="section hero">
  <div class="hero-photo" role="img" aria-label="Photo of a young child drawing with a pencil at a table"></div>
  <h1 class="heading hero-title">Lorem ipsum<br>dolor sit amet,<br>consectetuer</h1>
  <a class="btn" href="#">Find out more</a>
</section>

<section class="section about">
  <h2 class="heading about-title">A little bit about us...</h2>
  <p class="about-text">Lorem ipsum dolor sit amet, consectetur adipiscing elit, sed do eiusmod duopor<br>tempor incididunt ut labore et dolore magna aliqua. Quis ipsum suspend<br>isse ultrices gravida. Risus commodo</p>
  <a class="btn" href="#">Find out more</a>
</section>

<section class="section services">
  <div class="services-bg"></div>
  <svg class="services-photo" width="540" height="651" viewBox="0 0 540 651" role="img" aria-label="Photo of a child painting with a brush beside a paint palette and tin">
    <defs>
      <linearGradient id="paintTones" x1="0" y1="0" x2="1" y2="1">
        <stop offset="0" stop-color="#d9d4cf"/>
        <stop offset="0.45" stop-color="#c9a793"/>
        <stop offset="0.75" stop-color="#b86a55"/>
        <stop offset="1" stop-color="#e6e1dc"/>
      </linearGradient>
    </defs>
    <path d="M0 0 H420 A501 501 0 0 1 420 651 H0 Z" fill="url(#paintTones)"/>
  </svg>
  <h2 class="heading services-title">What we can do for<br>you and your child</h2>
  <p class="column-text services-text">Lorem ipsum dolor sit amet, consecte-<br>tur adipiscing elit, sed do eiusmod<br>tempor incididunt ut labore et dolore<br>magna aliqua. Quis ipsum suspendis-<br>se ultrices gravida. Risus commodo</p>
  <a class="btn" href="#">Find out more</a>
</section>

<section class="section checklist">
  <h2 class="heading checklist-title">Please ensure<br>your child brings...</h2>
  <p class="column-text checklist-text">Lorem ipsum dolor sit amet, consecte-<br>tur adipiscing elit, sed do eiusmod<br>tempor incididunt ut labore et dolore<br>magna aliqua. Quis ipsum suspendis-<br>se ultrices gravida. Risus commodo</p>
  <a class="btn" href="#">Find out more</a>

  <div class="item" style="top:147px">
    <svg class="item-icon" viewBox="0 0 128 128" aria-hidden="true">
      <circle cx="64" cy="64" r="61" fill="none" stroke="var(--green)" stroke-width="4"/>
      <g fill="none" stroke="var(--blue)" stroke-width="3.5" stroke-linejoin="round">
        <rect x="53" y="30" width="22" height="10" rx="2"/>
        <path d="M50 40 H78 V94 a4 4 0 0 1-4 4 H54 a4 4 0 0 1-4-4 Z"/>
        <path d="M50 58 H62 M50 76 H62"/>
      </g>
    </svg>
    <div class="item-title">Water to stay hydrated</div>
    <div class="item-text">Lorem ipsum dolor sit amet,<br>consectetur adipiscing elit,</div>
  </div>

  <div class="item" style="top:311px">
    <svg class="item-icon" viewBox="0 0 128 128" aria-hidden="true">
      <circle cx="64" cy="64" r="61" fill="none" stroke="var(--green)" stroke-width="4"/>
      <g fill="none" stroke="var(--blue)" stroke-width="3.5" stroke-linejoin="round" stroke-linecap="round">
        <path d="M34 58 C34 40 94 40 94 58 Z"/>
        <path d="M32 66 C40 60 48 72 56 66 C64 60 72 72 80 66 C86 62 92 66 96 66"/>
        <rect x="34" y="74" width="60" height="12" rx="6"/>
      </g>
    </svg>
    <div class="item-title">Enough food to last the day</div>
    <div class="item-text">Lorem ipsum dolor sit amet,<br>consectetur adipiscing elit,</div>
  </div>

  <div class="item" style="top:475px">
    <svg class="item-icon" viewBox="0 0 128 128" aria-hidden="true">
      <circle cx="64" cy="64" r="61" fill="none" stroke="var(--green)" stroke-width="4"/>
      <g fill="none" stroke="var(--blue)" stroke-width="3.5" stroke-linejoin="round">
        <rect x="50" y="32" width="28" height="10" rx="2"/>
        <rect x="44" y="42" width="40" height="56" rx="5"/>
        <path d="M64 58 V82 M52 70 H76"/>
      </g>
    </svg>
    <div class="item-title">Medication if needed</div>
    <div class="item-text">Lorem ipsum dolor sit amet,<br>consectetur adipiscing elit,</div>
  </div>
</section>

<section class="section banner">
  <div class="banner-photo" role="img" aria-label="Blue-tinted photo of children drawing together at a classroom table"></div>
  <h2 class="banner-title">Lorem ipsum dolor</h2>
  <p class="banner-text">Lorem ipsum dolor sit amet, consectetur adipiscing elit, sed do eius-<br>mod tempor incididunt ut labore et dolore magna aliqua.</p>
  <a class="btn" href="#">Find out more</a>
</section>

<section class="section gallery">
  <h2 class="heading gallery-title">Lorem ipsum dolar<br>sit amet, consect</h2>
  <p class="column-text gallery-text">Lorem ipsum dolor sit amet, consecte-<br>tur adipiscing elit, sed do eiusmod<br>tempor incididunt ut labore et dolore<br>magna aliqua. Quis ipsum suspendis-<br>se ultrices gravida. Risus commodo</p>
  <a class="btn" href="#">Find out more</a>
  <div class="snapshot snapshot-back"><div class="snapshot-fill" role="img" aria-label="Snapshot of children walking across a grassy field"></div></div>
  <div class="snapshot snapshot-front"><div class="snapshot-fill" role="img" aria-label="Snapshot of a child playing on a rope climbing frame"></div></div>
</section>

<footer class="section footer">
  <span class="social" style="left:469px" aria-label="Social link"></span>
  <span class="social" style="left:552px" aria-label="Social link"></span>
  <span class="social" style="left:638px" aria-label="Social link"></span>

  <div class="contact">
    <svg style="left:86px;top:-4px" width="26" height="34" viewBox="0 0 26 34" aria-hidden="true">
      <path d="M13 1 C6 1 1 6 1 13 C1 22 13 33 13 33 C13 33 25 22 25 13 C25 6 20 1 13 1 Z" fill="var(--white)"/>
      <circle cx="13" cy="13" r="5" fill="var(--green)"/>
    </svg>
    <span style="left:128px">Lorem ipsum dolor sit amet, AB1 2CD</span>
    <span style="left:505px">|</span>
    <svg style="left:540px;top:0" width="28" height="28" viewBox="0 0 28 28" aria-hidden="true">
      <path d="M6 2 L11 2 L13 9 L9 12 C11 17 13 19 17 20 L20 16 L27 18 L27 23 C27 25 25 27 22 27 C11 26 2 17 1 7 C1 4 3 2 6 2 Z" fill="var(--white)"/>
    </svg>
    <span style="left:578px">+44 1234 567890</span>
    <span style="left:755px">|</span>
    <svg style="left:790px;top:0" width="40" height="28" viewBox="0 0 40 28" aria-hidden="true">
      <rect x="2" y="2" width="36" height="24" fill="none" stroke="var(--white)" stroke-width="2.5"/>
      <path d="M2 2 L20 16 L38 2" fill="none" stroke="var(--white)" stroke-width="2.5"/>
    </svg>
    <span style="left:845px">hello@littleharbour.com</span>
  </div>

  <p class="copyright">Copyright © Little Harbour Childcare. All rights reserved</p>
</footer>

</body>
</html>
```